Pharmacy ad

need 2 pharmacy ads for the phone book. one for Birchfield Pharmacy and one for Corvane Rx Pharmacy. Dimensions for ad is 4.75in x 4.667 in. please see attached examples of ad uploaded as well logos of each pharmacy

```html
<!DOCTYPE html>
<html lang="en">
<head>
<meta charset="utf-8">
<title>Birchfield Pharmacy – Phone Book Ad</title>
<link href="https://fonts.googleapis.com/css2?family=Montserrat:wght@600;700;800&family=Roboto+Condensed:wght@700&family=Titillium+Web:ital,wght@0,400;0,600;1,400;1,600;1,700&display=swap" rel="stylesheet">
<style>
  :root {
    --green: #5aa02c;
    --green-bright: #4f9a0e;
    --green-light: #8cc63f;
    --navy: #2b2a45;
    --orange: #f7941d;
    --orange-deep: #f26522;
    --yellow: #fdd835;
    --red: #e30613;
    --white: #ffffff;
    --ink: #333333;
  }
  html, body { margin: 0; padding: 0; overflow: hidden; background: var(--white); }
  .ad {
    position: relative;
    width: 1200px;
    height: 1180px;
    overflow: hidden;
    background: var(--white);
    font-family: "Titillium Web", sans-serif;
  }
  .abs { position: absolute; }

  /* Brand block */
  .brand-mark {
    left: 150px; top: 82px; width: 96px; height: 96px;
    border-radius: 50%; background: var(--green-light);
  }
  .brand-name {
    left: 40px; top: 200px; width: 300px; text-align: center;
    font-family: "Montserrat", sans-serif; font-weight: 700;
    color: var(--navy); font-size: 38px; line-height: 44px; letter-spacing: 1px;
  }
  .brand-tagline {
    left: 40px; top: 296px; width: 300px; text-align: center;
    color: var(--green); font-style: italic; font-size: 15px;
  }

  /* Headline */
  .headline {
    left: 400px; top: 52px; margin: 0;
    font-family: "Montserrat", sans-serif; font-weight: 700;
    font-size: 76px; line-height: 66px; letter-spacing: 1px;
  }
  .headline .line-1 { color: var(--green); display: block; }
  .headline .line-2 { color: var(--navy); display: block; }

  /* Discount */
  .discount-figure {
    left: 404px; top: 196px;
    font-family: "Montserrat", sans-serif; font-weight: 600;
    font-size: 132px; line-height: 130px; letter-spacing: -4px;
    background: linear-gradient(180deg, #fdb913 0%, #f7941d 60%, #f26522 100%);
    -webkit-background-clip: text; background-clip: text; color: transparent;
  }
  .discount-label {
    left: 428px; top: 322px;
    color: var(--orange); font-style: italic; font-weight: 600;
    font-size: 36px; line-height: 40px;
  }
  .discount-tag { left: 700px; }
  .discount-tag svg { display: block; }
  .discount-tag .tag-text {
    position: absolute; left: 22px; top: 6px;
    color: var(--white); font-style: italic; font-size: 27px; line-height: 26px;
  }
  .discount-tag .tag-text strong { font-weight: 700; display: block; }
  .tag-senior { top: 222px; }
  .tag-student { top: 294px; }

  /* Services */
  .services { left: 110px; top: 402px; margin: 0; padding: 0; list-style: none; }
  .services li {
    display: flex; align-items: center; height: 56.5px;
    font-family: "Roboto Condensed", sans-serif; font-weight: 700;
    font-size: 33px; color: var(--green-bright);
  }
  .services li svg { width: 34px; height: 30px; margin-right: 16px; }

  /* Photo */
  .family-photo {
    left: 640px; top: 405px; width: 560px; height: 570px;
    background:
      radial-gradient(ellipse at 55% 45%, rgba(120,80,60,0.55) 0%, rgba(230,110,90,0.35) 45%, rgba(255,255,255,0) 72%),
      linear-gradient(180deg, rgba(255,255,255,0) 70%, #ffffff 100%);
  }

  /* Hours */
  .hours-badge { left: 107px; top: 883px; }
  .hours { top: 884px; font-style: italic; font-size: 30px; line-height: 30px; }
  .hours .day { font-weight: 600; display: block; }
  .hours .time { color: var(--navy); font-weight: 600; display: block; }
  .hours-week { left: 202px; }
  .hours-week .day { color: var(--green-bright); }
  .hours-sat { left: 541px; }
  .hours-sat .day { color: var(--orange); }
  .hours-sun { left: 766px; }
  .hours-sun .day { color: var(--red); }
  .hours-sun .time { font-weight: 400; color: var(--ink); }

  /* Contact band */
  .contact-band {
    left: 0; top: 972px; width: 1200px; height: 112px;
    background: linear-gradient(90deg, #f7941d 0%, #fbb03b 40%, #f7941d 50%, #fbb03b 70%, #f7941d 100%);
  }
  .band-divider { left: 598px; top: 972px; width: 4px; height: 112px; background: var(--white); }
  .branch-address {
    color: var(--white); font-style: italic; font-weight: 700;
    font-size: 27px; line-height: 24px;
  }
  .branch-address small { display: block; font-weight: 400; font-size: 20px; line-height: 20px; }
  .branch-main { left: 25px; top: 984px; }
  .branch-harbour { left: 640px; top: 994px; }
  .branch-phone {
    display: flex; align-items: center; gap: 20px;
    font-family: "Montserrat", sans-serif; font-weight: 700;
    font-size: 56px; color: var(--white); letter-spacing: 2px;
  }
  .phone-main { left: 232px; top: 992px; }
  .phone-harbour { left: 832px; top: 992px; }

  /* Footer */
  .footer { left: 20px; top: 1104px; width: 1160px; height: 56px; display: flex; align-items: center; }
  .footer .accept { font-style: italic; font-size: 26px; color: var(--ink); margin-right: 22px; }
  .partner { font-weight: 700; font-size: 22px; margin-right: 26px; color: var(--navy); }
  .partner.green { color: var(--green-bright); }
  .social { margin-left: auto; display: flex; align-items: center; gap: 8px; }
  .social .visit { font-weight: 700; font-size: 32px; color: var(--green-bright); }
  .social .on { font-style: italic; font-size: 24px; color: var(--ink); }
  .social .square { width: 30px; height: 30px; background: #3b5998; border-radius: 4px; }
  .social .page { font-style: italic; font-weight: 700; font-size: 26px; color: var(--navy); }
</style>
</head>
<body>
<div class="ad">

  <div class="abs brand-mark"></div>
  <div class="abs brand-name">BIRCHFIELD PHARMACY</div>
  <div class="abs brand-tagline">We Care About Your Health</div>

  <h1 class="abs headline">
    <span class="line-1">WE CARE ABOUT</span>
    <span class="line-2">YOUR HEALTH</span>
  </h1>

  <div class="abs discount-figure">10%</div>
  <div class="abs discount-label">DISCOUNT ON</div>

  <div class="abs discount-tag tag-senior">
    <svg width="420" height="66" viewBox="0 0 420 66">
      <polygon points="6,6 420,6 376,66 6,66" fill="#cccccc" opacity="0.5"/>
      <polygon points="0,0 412,0 370,62 0,62" fill="#4f9a0e"/>
    </svg>
    <div class="tag-text"><strong>Senior Citizen discount</strong>for patients 60 years &amp; over</div>
  </div>
  <div class="abs discount-tag tag-student">
    <svg width="300" height="66" viewBox="0 0 300 66">
      <polygon points="6,6 300,6 258,66 6,66" fill="#cccccc" opacity="0.5"/>
      <polygon points="0,0 290,0 250,64 0,64" fill="#8cc63f"/>
    </svg>
    <div class="tag-text"><strong>Student discount</strong>with valid ID card</div>
  </div>

  <ul class="abs services">
    <li><svg viewBox="0 0 34 30"><polyline points="3,16 13,26 31,3" fill="none" stroke="#2b2a45" stroke-width="5" stroke-linecap="round" stroke-linejoin="round"/></svg>Certified Pharmacists</li>
    <li><svg viewBox="0 0 34 30"><polyline points="3,16 13,26 31,3" fill="none" stroke="#2b2a45" stroke-width="5" stroke-linecap="round" stroke-linejoin="round"/></svg>Affordable prices</li>
    <li><svg viewBox="0 0 34 30"><polyline points="3,16 13,26 31,3" fill="none" stroke="#2b2a45" stroke-width="5" stroke-linecap="round" stroke-linejoin="round"/></svg>Brand and Generic Medicines</li>
    <li><svg viewBox="0 0 34 30"><polyline points="3,16 13,26 31,3" fill="none" stroke="#2b2a45" stroke-width="5" stroke-linecap="round" stroke-linejoin="round"/></svg>Blood Pressure and Glucose checks</li>
    <li><svg viewBox="0 0 34 30"><polyline points="3,16 13,26 31,3" fill="none" stroke="#2b2a45" stroke-width="5" stroke-linecap="round" stroke-linejoin="round"/></svg>Personal care and Beauty Products</li>
    <li><svg viewBox="0 0 34 30"><polyline points="3,16 13,26 31,3" fill="none" stroke="#2b2a45" stroke-width="5" stroke-linecap="round" stroke-linejoin="round"/></svg>Injectables</li>
    <li><svg viewBox="0 0 34 30"><polyline points="3,16 13,26 31,3" fill="none" stroke="#2b2a45" stroke-width="5" stroke-linecap="round" stroke-linejoin="round"/></svg>Special Orders</li>
    <li><svg viewBox="0 0 34 30"><polyline points="3,16 13,26 31,3" fill="none" stroke="#2b2a45" stroke-width="5" stroke-linecap="round" stroke-linejoin="round"/></svg>Delivery service</li>
  </ul>

  <div class="abs family-photo" role="img" aria-label="Photo of a smiling family of four: father, mother, young son and daughter, fading into white"></div>

  <svg class="abs hours-badge" width="68" height="68" viewBox="0 0 68 68">
    <circle cx="34" cy="34" r="34" fill="#fdd835"/>
    <polyline points="23,30 33,42 46,22" fill="none" stroke="#2b2a45" stroke-width="3" stroke-linecap="round" stroke-linejoin="round"/>
  </svg>
  <div class="abs hours hours-week"><span class="day">Monday to Friday</span><span class="time">10am- 6pm</span></div>
  <div class="abs hours hours-sat"><span class="day">Saturday</span><span class="time">10am-5pm</span></div>
  <div class="abs hours hours-sun"><span class="day">Sunday 10am-2pm</span><span class="time">(Larkin Street branch)</span></div>

  <div class="abs contact-band"></div>
  <div class="abs band-divider"></div>

  <div class="abs branch-address branch-main">27 Larkin Street,<br>Eastmoor<small>(opposite Grace<br>Chapel)</small></div>
  <div class="abs branch-phone phone-main">
    <svg width="42" height="42" viewBox="0 0 24 24"><path d="M6.6 10.8c1.4 2.8 3.8 5.1 6.6 6.6l2.2-2.2c.3-.3.7-.4 1-.2 1.1.4 2.3.6 3.6.6.6 0 1 .4 1 1V20c0 .6-.4 1-1 1C10.6 21 3 13.4 3 4c0-.6.4-1 1-1h3.5c.6 0 1 .4 1 1 0 1.3.2 2.5.6 3.6.1.3 0 .7-.2 1L6.6 10.8z" fill="#f26522"/></svg>
    555-0142
  </div>

  <div class="abs branch-address branch-harbour">Harbour Point,<br>Food Court<br>Eastmoor</div>
  <div class="abs branch-phone phone-harbour">
    <svg width="42" height="42" viewBox="0 0 24 24"><path d="M6.6 10.8c1.4 2.8 3.8 5.1 6.6 6.6l2.2-2.2c.3-.3.7-.4 1-.2 1.1.4 2.3.6 3.6.6.6 0 1 .4 1 1V20c0 .6-.4 1-1 1C10.6 21 3 13.4 3 4c0-.6.4-1 1-1h3.5c.6 0 1 .4 1 1 0 1.3.2 2.5.6 3.6.1.3 0 .7-.2 1L6.6 10.8z" fill="#f26522"/></svg>
    555-0178
  </div>

  <div class="abs footer">
    <span class="accept">We accept</span>
    <span class="partner">Crestpay</span>
    <span class="partner">Norcard</span>
    <span class="partner">Alder Life</span>
    <span class="partner green">Harborline</span>
    <div class="social">
      <span class="visit">Visit</span>
      <span class="on">us on</span>
      <span class="square"></span>
      <span class="page">Linkvine</span>
    </div>
  </div>

</div>
</body>
</html>
```